Chateau de Morvellac multiple flyers

PRICE OFFERED IS PER FLYER IE: €139 PER FLYER OR €695 TOTAL WITH OTHERS TO FOLLOW

I want to creat a common design across a range of flyers that I will be handing out to visitors to our Christmas market, but will also be used throughout the year and years to come. The final design will need to be adapted so the copy can be translated into french as well as English. So I would need an ai or paint version as well as pdf's etc.

There are 5 flyers to be designed at this stage the PRICE OFFERED IS PER FLYER IE: €139 PER FLYER OR €695 TOTAL WITH OTHERS TO FOLLOW

1. Seminars at the chateau - 4 page 1/3 A4 double sided (No longer referring to full chateau rental)
2. Accomodation at the chateau 2 page 1/3 A4 double sided (Seasons simplified now: Peak = July & August and Christmas week; High, June and September. Low: Rest of year.)
3. QVEB 2 Award in Wine and Spirits 4 page 1/3 A4 double sided
See current offering at
http://www.vinbrume-example.com/experiences-and-tours/wine-tours/qveb-level-2-loire-valley-peter-galloway/#1467282665644-f1124b7e-5513

With photos here:
https://www.filevault-example.com/sh/abc123defgh4567/AAAPxxxxxxxxxxxxxxxxxxxx?dl=0

4. Valentine's/Romantic package 2 page 1/3 A4 double sided
5. Mothers Day package 2 page 1/3 A4 double sided.

The first two are very urgent as need to be available by Wednesday 7th December to go to print.

In the future we will be looking to add to the range with:

6. Wedding Brochure - 6 page 1/3 A4 double sided
7. Group celebrations - 6 page 1/3 A4 double sided
8. Pamper/Wellness package - 2 page 1/3 A4 double sided
9. Activity Break - 2 page 1/3 A4 double sided.

I have attached some examples of what we have to date, which are not consistent. As well as some excel spreadhseets which explain the packages. Along with an architects plan of the ground floor (may help with the seminar brochure.)

I have also provided a link to our gallery of photos that can be used and a couple of videos to give you a feel for the place.

https://www.filevault-example.com/sh/zyx987wvuts6543/AACFyyyyyyyyyyyyyyyyyyyy?dl=0

Target Market(s)

Adults aged 34 plus.
Seminars = Local businesses
Accommodation = 34 plus high income
Wedding = Females 28 plus high income

Requirements
Must have
• Demonstrates 5 star luxury and quality.

```html
<!DOCTYPE html>
<html lang="en">
<head>
<meta charset="utf-8">
<title>Chateau de Morvellac – Price List</title>
<link href="https://fonts.googleapis.com/css2?family=Cormorant+Garamond:wght@500;600&family=Playfair+Display:wght@500&family=Libre+Baskerville:wght@400;700&family=Lato:wght@400;700&display=swap" rel="stylesheet">
<style>
  :root {
    --backdrop: #eceee6;
    --paper: #ffffff;
    --ink: #2b2b2b;
    --ink-soft: #5a5a5a;
    --gold: #c9a25a;
    --gold-light: #d4b47a;
    --rule: #cfc6b4;
    --plan-tone: #b9b9b9;
  }
  * { box-sizing: border-box; margin: 0; padding: 0; }
  html, body { width: 1200px; height: 701px; overflow: hidden; }
  body {
    background: var(--backdrop);
    display: flex; align-items: center; justify-content: center;
    font-family: "Libre Baskerville", Georgia, serif;
    color: var(--ink);
  }
  .page {
    width: 470px; height: 665px;
    background: var(--paper);
    box-shadow: 0 6px 24px rgba(0,0,0,.12);
    padding: 28px 30px 22px;
    position: relative;
    display: flex; flex-direction: column;
  }
  .brand {
    text-align: center;
    font-family: "Cormorant Garamond", Georgia, serif;
    font-weight: 600; font-size: 15px; letter-spacing: .28em;
    text-transform: uppercase; color: var(--ink);
  }
  .title {
    text-align: center;
    font-family: "Playfair Display", Georgia, serif;
    font-weight: 500; font-size: 30px; color: var(--gold);
    margin: 10px 0 16px;
  }
  .price-table { width: 100%; border-collapse: collapse; font-size: 7.2px; }
  .price-table th {
    font-family: "Lato", Arial, sans-serif; font-weight: 700;
    font-size: 7.4px; text-align: left; padding: 0 3px 4px;
    border-bottom: 1px solid var(--gold); vertical-align: bottom; line-height: 1.25;
  }
  .price-table th.space-head { font-size: 10px; }
  .price-table td { padding: 2.4px 3px; color: var(--ink-soft); }
  .price-table td.space { color: var(--ink); }
  .price-table tbody tr:last-child td { border-bottom: 1px solid var(--gold); }
  .lower { display: flex; gap: 18px; margin-top: 28px; }
  .discount-box {
    flex: 0 0 210px; background: var(--gold-light);
    padding: 14px 14px; font-size: 7.6px; line-height: 1.65; color: var(--ink);
  }
  .discount-box ol { padding-left: 12px; margin-top: 4px; }
  .plans { flex: 1; display: flex; flex-direction: column; gap: 10px; }
  .plan { background: linear-gradient(90deg, #d8d8d8, var(--plan-tone)); }
  .plan-upper { height: 52px; }
  .plan-lower { height: 44px; width: 80%; }
  .plan-caption { font-size: 7.2px; line-height: 1.6; color: var(--ink); margin-top: 4px; }
  .folio {
    position: absolute; right: 30px; bottom: 18px;
    font-family: "Lato", Arial, sans-serif; font-size: 7px; color: var(--ink-soft);
  }
</style>
</head>
<body>
  <article class="page">
    <header>
      <div class="brand">Chateau de Morvellac</div>
      <h1 class="title">Price List</h1>
    </header>

    <table class="price-table">
      <thead>
        <tr>
          <th class="space-head">Function Space</th>
          <th>Seating<br>capacity</th>
          <th>Day rate<br>(HT)</th>
          <th>½ Day<br>(HT)</th>
          <th>2 Days<br>(HT)</th>
          <th>Weekend<br>(HT)</th>
          <th>Week<br>(HT)</th>
        </tr>
      </thead>
      <tbody>
        <tr><td class="space">Salon de Réception</td><td>120</td><td>950</td><td>600</td><td>1800</td><td>2400</td><td>5200</td></tr>
        <tr><td class="space">Grand Salon</td><td>80</td><td>750</td><td>450</td><td>1400</td><td>1900</td><td>4100</td></tr>
        <tr><td class="space">Library</td><td>30</td><td>400</td><td>250</td><td>750</td><td>1000</td><td>2200</td></tr>
        <tr><td class="space">Dining Room</td><td>60</td><td>600</td><td>380</td><td>1150</td><td>1500</td><td>3300</td></tr>
        <tr><td class="space">Billiard Room</td><td>20</td><td>300</td><td>180</td><td>560</td><td>750</td><td>1600</td></tr>
        <tr><td class="space">Orangery</td><td>90</td><td>800</td><td>500</td><td>1500</td><td>2000</td><td>4400</td></tr>
        <tr><td class="space">Chapel</td><td>50</td><td>450</td><td>280</td><td>850</td><td>1150</td><td>2500</td></tr>
        <tr><td class="space">Terrace</td><td>100</td><td>650</td><td>400</td><td>1250</td><td>1650</td><td>3600</td></tr>
        <tr><td class="space">Courtyard</td><td>150</td><td>700</td><td>450</td><td>1350</td><td>1800</td><td>3900</td></tr>
        <tr><td class="space">Park</td><td>300</td><td>1200</td><td>750</td><td>2300</td><td>3000</td><td>6500</td></tr>
        <tr><td class="space">Wine Cellar</td><td>40</td><td>500</td><td>300</td><td>950</td><td>1250</td><td>2700</td></tr>
        <tr><td class="space">Ground Floor</td><td>200</td><td>1900</td><td>1200</td><td>3600</td><td>4800</td><td>9800</td></tr>
        <tr><td class="space">Full Chateau</td><td>250</td><td>2900</td><td>1800</td><td>5500</td><td>7300</td><td>14900</td></tr>
      </tbody>
    </table>

    <section class="lower">
      <div class="discount-box">
        As part of our Corporate Social Responsibility the Chateau offers a 10% discount to the following:
        <ol>
          <li>Charities and local associations</li>
          <li>Businesses of under ten staff</li>
          <li>Schools and training bodies</li>
          <li>Events booked over four months ahead</li>
          <li>Returning clients of the chateau</li>
          <li>Events held on weekdays only</li>
        </ol>
      </div>
      <div class="plans">
        <div class="plan plan-upper" role="img" aria-label="Architect's ground floor plan of the chateau, upper section"></div>
        <div class="plan plan-lower" role="img" aria-label="Architect's ground floor plan of the chateau, lower wing"></div>
        <p class="plan-caption">You can use all the dining rooms, ground floor salons and gardens with these flexible options for your company events and seminars.</p>
      </div>
    </section>

    <footer class="folio">Page 34</footer>
  </article>
</body>
</html>
```